Harriet Voss Consortium - Paediatric Lower Limb Surgery Agenda Forming Collective

A 2-sided A4 leaflet to explain the research priorities in Children's Orthopaedic Surgery.
We would like this to be similar to that produced previously by the physiotherapists.

```html
<!DOCTYPE html>
<html lang="en">
<head>
<meta charset="utf-8">
<title>Harriet Voss Consortium – Research Priorities</title>
<link href="https://fonts.googleapis.com/css2?family=Arimo:ital,wght@0,400;0,700;1,700&display=swap" rel="stylesheet">
<style>
:root{
  --navy:#3c4690;
  --navy-deep:#262d6e;
  --magenta:#c3428c;
  --teal:#2bb3b6;
  --orange:#f5a31f;
  --pink-text:#b5327c;
  --ink:#3a3a48;
  --page:#f3f3f3;
  --backdrop:#d6d6d6;
  --white:#ffffff;
}
*{margin:0;padding:0;box-sizing:border-box}
html,body{width:1200px;height:4688px;overflow:hidden}
body{background:var(--backdrop);font-family:"Arimo",Arial,sans-serif;position:relative}
.leaflet{position:absolute;left:140px;top:62px;width:922px;height:4563px;background:var(--page);box-shadow:0 0 18px rgba(0,0,0,.18)}
.masthead{position:absolute;left:0;top:0;width:922px;height:485px}
.masthead svg{position:absolute;inset:0}
.brand-row{position:absolute;left:50px;right:40px;top:45px;display:flex;justify-content:space-between;align-items:center}
.society{display:flex;align-items:center;gap:18px;color:var(--white);font-size:20px;line-height:1.15;font-weight:700;text-transform:uppercase}
.society .mark{width:92px;height:92px;border-radius:50%;border:8px solid var(--white)}
.partners{display:flex;align-items:center;gap:22px;color:var(--white);font-size:19px;font-weight:700;line-height:1.2}
.partners .badge{width:80px;height:80px;border-radius:50%;background:rgba(255,255,255,.35)}
.title{position:absolute;left:60px;top:235px;color:var(--white);font-size:50px;line-height:60px;font-weight:400}
.intro{position:absolute;left:50px;width:820px;top:545px;color:var(--pink-text);font-size:26px;line-height:31px}
.intro p+p{margin-top:40px}
.stage{position:absolute;top:891px;color:var(--white);padding:22px 20px;border-radius:26px 26px 0 26px;font-size:22px;line-height:27px}
.stage h3{font-size:38px;font-weight:700;text-align:right;margin-bottom:8px}
.stage-ask{left:0;width:282px;height:453px;background:var(--teal)}
.stage-analyse{left:313px;width:297px;height:329px;background:var(--magenta);border-radius:26px}
.stage-prioritise{left:626px;width:296px;height:453px;background:var(--orange);border-radius:26px 26px 26px 0}
.priorities-heading{position:absolute;left:0;width:922px;top:1443px;text-align:center;color:var(--magenta);font-size:32px;font-weight:700}
.priority{position:absolute;left:0;width:922px}
.priority svg{position:absolute;inset:0;width:100%;height:100%}
.priority .num{position:absolute;top:50%;transform:translateY(-50%);font-size:140px;line-height:1;font-weight:400}
.priority p{position:absolute;top:50%;transform:translateY(-50%);color:var(--ink);font-size:25px;line-height:31px}
.priority.left .num{left:30px}
.priority.left p{left:150px;width:720px}
.priority.right .num{right:40px}
.priority.right p{left:50px;width:710px}
.priority.wide-num p{width:600px}
.closing{position:absolute;left:50px;width:830px;top:4140px;color:var(--navy);font-size:25px;line-height:31px;font-style:italic;font-weight:700}
.thanks{position:absolute;left:50px;width:840px;top:4265px;color:var(--magenta);font-size:25px;line-height:31px}
.thanks ul{list-style:none;margin-top:8px}
.thanks li::before{content:"•";margin-right:14px}
</style>
</head>
<body>
<main class="leaflet">
  <header class="masthead">
    <svg viewBox="0 0 922 485" preserveAspectRatio="none" aria-hidden="true">
      <defs><linearGradient id="headGrad" x1="0" y1="0" x2="0" y2="1"><stop offset="0" stop-color="#4a4fa0"/><stop offset="1" stop-color="#232a6b"/></linearGradient></defs>
      <polygon points="0,0 922,0 922,430 461,485 0,430" fill="url(#headGrad)"/>
    </svg>
    <div class="brand-row">
      <div class="society"><span class="mark"></span><span>Allied Society<br>of Movement<br>Therapy</span></div>
      <div class="partners"><span class="badge"></span><span>Northgate Society<br>University of Kestrelford</span></div>
    </div>
    <h1 class="title">Harriet Voss Consortium<br>Paediatric Lower Limb Surgery<br>Agenda Forming Collective</h1>
  </header>

  <section class="intro">
    <p>Surgery is often carried out amongst children with conditions that their legs, but inmany conditions,it is not known which treatment works best. We need high-quality research to test which treatments are better for children.</p>
    <p>We reached out to everybody involved with children who have orthopaedic problems affecting their legs (from hip to toes), including children, parents, carers, charity workers, and all the professional groups. We asked all for their views on identifying the most important unanswered questions.</p>
  </section>

  <div class="stage stage-ask"><h3>Stage 1</h3>ASK – Our UK-wide survey of patients, carers, physiotherapists, nurses and surgeons asked "What is the most important unanswered question amongst children undergoing planned surgery for conditions affecting their legs"</div>
  <div class="stage stage-analyse"><h3>Stage 2</h3>ANALYSE – We reviewed 1023 questions from 388 people, and sorted these into 76 unique themed questions.</div>
  <div class="stage stage-prioritise"><h3>Stage 3</h3>PRIORITISE – From those we asked patients, carers, physiotherapists, nurses and surgeons to tell us "What are your top-10 most important questions". This created a shortlist that were prioritized at a final workshop.</div>

  <h2 class="priorities-heading">OUR TOP-10 RESEARCH PRIORITIES:</h2>

  <div class="priority left" style="top:1516px;height:322px">
    <svg viewBox="0 0 922 322" preserveAspectRatio="none" aria-hidden="true"><polygon points="0,20 922,0 922,290 0,322" fill="var(--navy)"/><polygon points="130,45 900,30 900,270 130,295" fill="#f7f7fa"/></svg>
    <span class="num" style="color:var(--orange)">1</span>
    <p>What are the best ways to measure the outcome following lower limb orthopaedic surgery in children?</p>
  </div>
  <div class="priority right" style="top:1850px;height:238px">
    <svg viewBox="0 0 922 238" preserveAspectRatio="none" aria-hidden="true"><polygon points="0,0 922,25 922,238 0,215" fill="var(--magenta)"/><polygon points="20,20 780,35 780,210 20,195" fill="#fbf3f8"/></svg>
    <span class="num" style="color:#f6d4e7">2</span>
    <p>Following orthopaedic surgery to the lower limbs, what should children's rehabilitation include, how long is it expected to last and how does it affect the result of treatment?</p>
  </div>
  <div class="priority left" style="top:2063px;height:256px">
    <svg viewBox="0 0 922 256" preserveAspectRatio="none" aria-hidden="true"><polygon points="0,20 922,0 922,230 0,256" fill="var(--teal)"/><polygon points="130,38 900,22 900,212 130,232" fill="#f4fbfb"/></svg>
    <span class="num" style="color:var(--orange)">3</span>
    <p>What is the short-term and long-term clinical and cost effectiveness of orthopaedic lower limb surgery (including best timing and technique) for children with Cerebral Palsy who can walk?</p>
  </div>
  <div class="priority right" style="top:2319px;height:238px">
    <svg viewBox="0 0 922 238" preserveAspectRatio="none" aria-hidden="true"><polygon points="0,0 922,25 922,238 0,215" fill="var(--orange)"/><polygon points="20,20 780,35 780,210 20,195" fill="#fffaf1"/></svg>
    <span class="num" style="color:var(--navy)">4</span>
    <p>What are the short term and long term outcomes of surgery compared to non-surgical care in the treatment of Perthes disease of the hip?</p>
  </div>
  <div class="priority left" style="top:2563px;height:250px">
    <svg viewBox="0 0 922 250" preserveAspectRatio="none" aria-hidden="true"><polygon points="0,20 922,0 922,225 0,250" fill="var(--navy)"/><polygon points="130,38 900,22 900,205 130,228" fill="#f7f7fa"/></svg>
    <span class="num" style="color:var(--orange)">5</span>
    <p>What is the clinical and cost effectiveness of pre-operative rehabilitation in children presenting with lower limb orthopaedic conditions?</p>
  </div>
  <div class="priority right" style="top:2800px;height:297px">
    <svg viewBox="0 0 922 297" preserveAspectRatio="none" aria-hidden="true"><polygon points="0,0 922,25 922,297 0,270" fill="var(--magenta)"/><polygon points="20,22 780,38 780,265 20,248" fill="#fbf3f8"/></svg>
    <span class="num" style="color:#f6d4e7">6</span>
    <p>What is the short-term and long-term clinical and cost effectiveness of Selective Dorsal Rhizotomy (SDR) in children with Cerebral Palsy who can walk?</p>
  </div>
  <div class="priority left" style="top:3094px;height:266px">
    <svg viewBox="0 0 922 266" preserveAspectRatio="none" aria-hidden="true"><polygon points="0,20 922,0 922,240 0,266" fill="var(--teal)"/><polygon points="130,38 900,22 900,220 130,244" fill="#f4fbfb"/></svg>
    <span class="num" style="color:var(--orange)">7</span>
    <p>Can surveillance and non-surgical treatment (e.g. physiotherapy, botulinum toxin injections, functional electrical stimulation, orthotics, casting) prevent the development of deformity requiring surgery in children with Cerebral Palsy?</p>
  </div>
  <div class="priority right" style="top:3330px;height:235px">
    <svg viewBox="0 0 922 235" preserveAspectRatio="none" aria-hidden="true"><polygon points="0,0 922,25 922,235 0,212" fill="var(--orange)"/><polygon points="20,20 780,35 780,208 20,192" fill="#fffaf1"/></svg>
    <span class="num" style="color:var(--navy)">8</span>
    <p>What is the best method of screening for Developmental Dysplasia of the Hip (DDH) in terms of clinical and cost effectiveness?</p>
  </div>
  <div class="priority left" style="top:3563px;height:250px">
    <svg viewBox="0 0 922 250" preserveAspectRatio="none" aria-hidden="true"><polygon points="0,20 922,0 922,225 0,250" fill="var(--navy)"/><polygon points="130,38 900,22 900,205 130,228" fill="#f7f7fa"/></svg>
    <span class="num" style="color:var(--orange)">9</span>
    <p>What are the best strategies to optimise communication of information between patients/carers and clinicians in order to enable shared decision-making?</p>
  </div>
  <div class="priority right wide-num" style="top:3766px;height:303px">
    <svg viewBox="0 0 922 303" preserveAspectRatio="none" aria-hidden="true"><polygon points="0,0 922,25 922,303 0,275" fill="var(--magenta)"/><polygon points="20,60 690,72 690,240 20,228" fill="#fbf3f8"/></svg>
    <span class="num" style="color:#f6d4e7">10</span>
    <p>What is the best management for hip displacement in children with Cerebral Palsy?</p>
  </div>

  <p class="closing">Many thanks to all those people who helped us take this work off the ground and helped us finish it!</p>
  <section class="thanks">
    <p>Special thanks to:</p>
    <ul>
      <li>The Northgate Society for Child Bone Surgery</li>
      <li>The National Bone &amp; Joint Guild</li>
      <li>The University of Kestrelford and the</li>
      <li>Harriet Voss Consortium, who always look for fair play in research!</li>
    </ul>
  </section>
</main>
</body>
</html>
```